Bright Harbor Health (03)

We're designing a website to sell Medicare Supplements. Attached is the script we want to say and general layout, but please use your best knowledge to make it better. This platform should be extremely user-friendly, but we want to make it look fun and approachable! Most Insurance/medicare websites are very boring, drab, simple but we want this one to be more personalized, fun and sexy (but again, still user-friendly since our target demographic is 65+).

This homepage should include a fun and inviting quiz, the script is in the attachment below. It should also include the blurbs about what medicare supplements plans are and why they should buy them. Feel free to play around with cool fonts and imagery, we want the site to be engaging!

Target Market(s)

seniors

Industry/Entity Type

Insurance

Number of Pages Required

1 page

Requirements
Must have
• Quiz, company name and tag line, script
Nice to have
• fun, engaging elements

```html
<!DOCTYPE html>
<html lang="en">
<head>
<meta charset="utf-8">
<title>Bright Harbor Health – Medicare Supplement Plans</title>
<link href="https://fonts.googleapis.com/css2?family=Bebas+Neue&family=Poppins:wght@400;500&family=Roboto:wght@400;500;700&display=swap" rel="stylesheet">
<style>
:root{
  --navy:#0d2235;
  --ink:#1b2b3a;
  --body:#555d66;
  --blue:#2f9df4;
  --sky:#31c6f7;
  --indigo:#4f7ee8;
  --soft:#f6f7fb;
  --white:#ffffff;
  --grad:linear-gradient(90deg,#5a7fe6 0%,#2fc4f7 100%);
}
*{margin:0;padding:0;box-sizing:border-box}
html,body{width:1200px;height:2844px;overflow:hidden}
body{position:relative;background:var(--white);font-family:"Poppins",sans-serif;color:var(--body)}
.abs{position:absolute}
.brand{font-family:"Roboto",sans-serif;font-weight:700;color:var(--navy)}

/* header */
.site-header{left:0;top:0;width:1200px;height:94px;background:var(--white)}
.site-header .brand{left:77px;top:31px;font-size:28px}
.call-box{left:923px;top:22px;display:flex;align-items:center;gap:10px}
.call-icon{width:52px;height:52px;border-radius:50%;border:2px solid #9fd3fa;display:flex;align-items:center;justify-content:center}
.call-icon span{width:42px;height:42px;border-radius:50%;background:var(--grad);display:flex;align-items:center;justify-content:center}
.call-label{font-family:"Roboto",sans-serif;font-size:14px;color:#555}
.call-number{font-family:"Roboto",sans-serif;font-weight:700;font-size:21px;color:var(--navy)}

/* hero */
.hero{left:0;top:94px;width:1200px;height:583px;background:linear-gradient(100deg,#4a4541 0%,#6b625a 35%,#a89b8e 60%,#c9c2b8 80%,#8f8377 100%)}
.hero-shade{left:0;top:94px;width:1200px;height:583px;background:linear-gradient(90deg,rgba(20,20,22,.55) 0%,rgba(20,20,22,.25) 45%,rgba(0,0,0,0) 70%)}
.hero-title{left:76px;top:278px;font-family:"Bebas Neue",sans-serif;font-size:42px;line-height:44px;color:var(--white);width:460px}
.hero-call{left:77px;top:420px;font-family:"Poppins",sans-serif;font-weight:500;font-size:31px;color:var(--sky)}
.hero-sub{left:79px;top:468px;font-family:"Roboto",sans-serif;font-size:18px;line-height:26px;color:var(--white);width:360px}
.arrow{width:52px;height:52px;border-radius:50%;display:flex;align-items:center;justify-content:center}
.arrow.prev{left:13px;top:359px;background:var(--grad)}
.arrow.next{left:1137px;top:359px;border:1.5px solid var(--white)}

/* zip */
.zip-form{left:246px;top:646px;width:708px;height:62px;display:flex;box-shadow:0 8px 24px rgba(30,60,120,.08)}
.zip-input{flex:1;background:var(--white);border-radius:4px 0 0 4px;font-size:14px;color:#555;padding:0 22px;display:flex;align-items:center}
.zip-btn{width:126px;background:var(--grad);color:var(--white);font-family:"Roboto",sans-serif;font-weight:700;font-size:22px;display:flex;align-items:center;justify-content:center;border-radius:0 4px 4px 0}

/* about */
.about{left:0;top:677px;width:1200px;height:946px;background:var(--soft);z-index:-1}
.section-title{font-family:"Roboto",sans-serif;font-weight:700;color:var(--navy)}
.about-title{left:0;top:766px;width:1200px;text-align:center;font-size:42px;line-height:47px}
.about-text{left:250px;top:886px;width:700px;text-align:center;font-size:14.5px;line-height:27px}
.about-text p+p{margin-top:9px}
.doctor-photo{left:158px;top:1074px;width:688px;height:479px;border-radius:6px;background:linear-gradient(120deg,#e9ecef 0%,#dfe3e6 35%,#c9b79a 70%,#a88f6c 100%)}
.benefit{left:670px;width:381px;background:var(--grad);border-radius:3px;color:var(--white);font-size:14.5px;line-height:25px;padding:0 18px 0 45px;display:flex;align-items:center}
.benefit::before{content:"";position:absolute;left:18px;top:calc(50% - 12px);width:12px;height:12px;border-radius:50%;background:var(--white)}
.benefit.b1{top:1116px;height:93px}
.benefit.b1::before{top:18px}
.benefit.b2{top:1224px;height:82px}
.benefit.b3{top:1324px;height:83px}
.benefit.b4{top:1423px;height:83px}

/* costs */
.costs-title{left:157px;top:1688px;font-size:41px;line-height:47px}
.costs-sub{left:157px;top:1793px;font-family:"Roboto",sans-serif;font-size:25px;color:var(--ink)}
.costs-text{left:541px;top:1692px;width:536px;font-size:15px;line-height:27.2px}
.card{top:1923px;width:292px;height:332px;background:var(--white);border-radius:6px;box-shadow:0 4px 24px rgba(20,40,80,.08);padding:28px 28px 0}
.card.c1{left:130px}.card.c2{left:455px}.card.c3{left:779px}
.card-icon{width:83px;height:83px;border-radius:50%;background:var(--grad);display:flex;align-items:center;justify-content:center}
.card h3{font-family:"Roboto",sans-serif;font-weight:700;font-size:20px;line-height:25px;color:var(--navy);margin-top:26px;min-height:50px}
.card p{font-size:14.5px;line-height:25px;margin-top:12px}

/* contact band */
.cta{left:0;top:2323px;width:1200px;height:291px;background:linear-gradient(90deg,#5a7ee5 0%,#3aa6f2 55%,#2fc6f8 100%);text-align:center;color:var(--white)}
.cta h2{font-family:"Roboto",sans-serif;font-weight:700;font-size:41px;margin-top:68px}
.cta p{font-size:18px;margin-top:6px}
.cta-btn{display:inline-block;margin-top:18px;width:178px;height:58px;line-height:58px;background:var(--white);border-radius:3px;font-family:"Roboto",sans-serif;font-weight:700;font-size:18px;color:var(--blue)}

/* footer */
.site-footer{left:0;top:2614px;width:1200px;height:230px;background:var(--soft)}
.footer-brand{left:80px;top:2666px;font-size:27px;line-height:28px;width:160px}
.foot-links{top:2661px;list-style:none;font-size:15px;line-height:29px;color:var(--body)}
.foot-links.l1{left:330px}.foot-links.l2{left:507px}.foot-links.l3{left:663px}
.contact-row{left:859px;display:flex;align-items:center;gap:14px}
.contact-row.phone{top:2646px}.contact-row.mail{top:2697px}
.ring{width:38px;height:38px;border-radius:50%;border:1.5px solid #b8c8f0;display:flex;align-items:center;justify-content:center}
.phone-text{font-family:"Roboto",sans-serif;font-size:22px;color:var(--blue)}
.phone-text b{font-weight:700;color:#2d6fe0}
.mail-text{font-size:15px;color:var(--ink)}
.foot-rule{left:80px;top:2776px;width:1040px;height:1px;background:#e3e6ee}
.copyright{left:80px;top:2800px;font-size:15px;color:var(--ink)}
.chat{left:1055px;top:2779px;width:66px;height:66px;border-radius:50%;background:var(--grad);display:flex;align-items:center;justify-content:center}
</style>
</head>
<body>

<header class="site-header abs">
  <div class="brand abs">Bright Harbor Health</div>
  <div class="call-box abs">
    <div class="call-icon"><span>
      <svg width="20" height="20" viewBox="0 0 24 24"><path fill="#fff" d="M6.6 10.8a15.1 15.1 0 0 0 6.6 6.6l2.2-2.2c.3-.3.7-.4 1-.2 1.1.4 2.3.6 3.6.6.6 0 1 .4 1 1V20c0 .6-.4 1-1 1A17 17 0 0 1 3 4c0-.6.4-1 1-1h3.5c.6 0 1 .4 1 1 0 1.3.2 2.5.6 3.6.1.3 0 .7-.2 1z"/></svg>
    </span></div>
    <div>
      <div class="call-label">Call Us Today :</div>
      <div class="call-number">555 214 3380</div>
    </div>
  </div>
</header>

<section>
  <div class="hero abs" role="img" aria-label="Photo of a smiling senior couple on a sofa looking at a laptop together"></div>
  <div class="hero-shade abs"></div>
  <h1 class="hero-title abs">Be Confident In Choosing The Medicare Supplement Plan That’s Right For You.</h1>
  <div class="hero-call abs">Call (800) 555-0147</div>
  <p class="hero-sub abs">For more information, or continue to view our premium plans</p>
  <div class="arrow prev abs"><svg width="16" height="22" viewBox="0 0 16 22"><path d="M11 3 4 11l7 8" fill="none" stroke="#fff" stroke-width="2"/></svg></div>
  <div class="arrow next abs"><svg width="16" height="22" viewBox="0 0 16 22"><path d="m5 3 7 8-7 8" fill="none" stroke="#fff" stroke-width="2"/></svg></div>
  <div class="zip-form abs">
    <div class="zip-input">Enter Your Zip *</div>
    <div class="zip-btn">FIND</div>
  </div>
</section>

<section>
  <div class="about abs"></div>
  <h2 class="section-title about-title abs">What is a Medicare<br>Supplement plan?</h2>
  <div class="about-text abs">
    <p>Each Medicare Supplement insurance plan offers a different level of basic benefits, but each lettered plan will include the same standardized basic benefits regardless of insurance company and location.</p>
    <p>Medicare Supplement insurance plans do not always cover vision, dental, long-term care, or hearing aids, but all plans must cover at least a portion of the following basic benefits:</p>
  </div>
  <div class="doctor-photo abs" role="img" aria-label="Photo of a doctor in a white coat writing on a form at a desk with a patient"></div>
  <div class="benefit b1 abs">Medicare Part A coinsurance costs up to an additional 365 days after Medicare benefits are exhausted</div>
  <div class="benefit b2 abs">Medicare Part A hospice care coinsurance or copayments</div>
  <div class="benefit b3 abs">Medicare Part B coinsurance or copayments</div>
  <div class="benefit b4 abs">First three pints of blood used in a medical procedure</div>
</section>

<section>
  <h2 class="section-title costs-title abs">Medicare<br>Supplement</h2>
  <div class="costs-sub abs">Insurance Plan Costs</div>
  <p class="costs-text abs">Although private insurance companies are required to offer the same basic benefits for each lettered plan, they do have the ability to charge different premiums. You might want to shop around to find a Medicare Supplement insurance plan that may fit your medical and financial needs. Insurance companies may price their plan premiums in any of the following ways:</p>

  <article class="card c1 abs">
    <div class="card-icon"><svg width="46" height="40" viewBox="0 0 46 40" fill="none" stroke="#fff" stroke-width="1.6"><circle cx="9" cy="7" r="4"/><circle cx="23" cy="7" r="4"/><circle cx="37" cy="7" r="4"/><path d="M4 36V18h10v18M18 36V18h10v18M32 36V18h10v18"/></svg></div>
    <h3>Community<br>No-Age-Rated:</h3>
    <p>These Medicare Supplement insurance plans charge premiums that are the same across the board, regardless of age.</p>
  </article>
  <article class="card c2 abs">
    <div class="card-icon"><svg width="44" height="40" viewBox="0 0 44 40" fill="none" stroke="#fff" stroke-width="1.6"><circle cx="15" cy="22" r="11"/><path d="M18 17h-4a2.5 2.5 0 0 0 0 5h2a2.5 2.5 0 0 1 0 5h-4M15 14v3M15 27v3M30 6c6 1 9 6 8 12l3 4-3 1v5h-5"/></svg></div>
    <h3>Issue-Age-Rated</h3>
    <p>These plans base their premiums on your age when you first enrolled in the policy.</p>
  </article>
  <article class="card c3 abs">
    <div class="card-icon"><svg width="44" height="40" viewBox="0 0 44 40" fill="none" stroke="#fff" stroke-width="1.6"><rect x="6" y="5" width="22" height="30" rx="2"/><path d="M11 13h12M11 19h12M11 25h8M26 22l12-6 3 4-12 7"/></svg></div>
    <h3>Attained-Age-Rated</h3>
    <p>Like issue-age-rated, these plans base their premiums on the age you were when you first bought a policy.</p>
  </article>
</section>

<section class="cta abs">
  <h2>Do you have any Question ?</h2>
  <p>Contact Us Now.</p>
  <span class="cta-btn">CONTACT US</span>
</section>

<footer class="site-footer abs"></footer>
<div class="brand footer-brand abs">Bright Harbor Health</div>
<ul class="foot-links l1 abs"><li>Supplyment</li><li>Plan Costs</li><li>Insurance</li></ul>
<ul class="foot-links l2 abs"><li>Login</li><li>Signup</li><li>Help</li></ul>
<ul class="foot-links l3 abs"><li>Privacy Policy</li><li>Tearms of Use</li></ul>
<div class="contact-row phone abs">
  <div class="ring"><svg width="18" height="18" viewBox="0 0 24 24"><path fill="#4f7ee8" d="M6.6 10.8a15.1 15.1 0 0 0 6.6 6.6l2.2-2.2c.3-.3.7-.4 1-.2 1.1.4 2.3.6 3.6.6.6 0 1 .4 1 1V20c0 .6-.4 1-1 1A17 17 0 0 1 3 4c0-.6.4-1 1-1h3.5c.6 0 1 .4 1 1 0 1.3.2 2.5.6 3.6.1.3 0 .7-.2 1z"/></svg></div>
  <div class="phone-text">+555-<b>214-3380</b></div>
</div>
<div class="contact-row mail abs">
  <div class="ring"><svg width="18" height="18" viewBox="0 0 24 24"><circle cx="12" cy="12" r="11" fill="#4f7ee8"/><path d="M6 8h12v8H6zM6 8l6 5 6-5" fill="none" stroke="#fff" stroke-width="1.4"/></svg></div>
  <div class="mail-text">hello@brightharborhealth.com</div>
</div>
<div class="foot-rule abs"></div>
<div class="copyright abs">©Bright Harbor Health - 2020 All rights Reserved.</div>
<div class="chat abs"><svg width="30" height="28" viewBox="0 0 30 28"><path d="M15 3C8 3 3 7.5 3 13c0 3 1.5 5.6 4 7.4L6 25l5.2-2.6c1.2.3 2.5.5 3.8.5 7 0 12-4.5 12-10S22 3 15 3z" fill="#fff"/></svg></div>

</body>
</html>
```